Anzeigengestaltung für ambulanten Pflegedienst
Zielgruppe
Es handelt sich um einen ambulanten Pflegedienst, der am 01. September 2024 einjähriges Jubiläum feiert. Von 10:00 Uhr bis 15:00 Uhr ist dazu im Büro in der Ginsterweg 14 in Dessau-Roßlau ein kleiner Empfang mit Kuchen und Getränken geplant.
Weiterhin benötige ich eine Anzeige, um einen Hauswirtschafter zu suchen.
Und eine Anzeige für Beratungen gem.

```html
<!DOCTYPE html>
<html lang="de">
<head>
<meta charset="utf-8">
<title>Anzeigen Lindwerk Pflege</title>
<link href="https://fonts.googleapis.com/css2?family=Montserrat:wght@400;500;600;700&family=Nunito+Sans:wght@400;600;700&family=Lora:wght@400&display=swap" rel="stylesheet">
<style>
:root{
  --teal:#1f6f78;
  --green:#5fae3c;
  --ink:#2f3a3d;
  --muted:#6b7679;
  --paper:#ffffff;
  --mist:#eef1f2;
  --footer:#dcebf0;
  --pill:#2a9aa5;
  --pill-text:#ffffff;
  --canvas:#ffffff;
}
*{box-sizing:border-box;margin:0;padding:0}
html,body{width:1200px;height:1200px;overflow:hidden;background:var(--canvas)}
body{font-family:"Nunito Sans",Arial,sans-serif;color:var(--ink);position:relative}
.row{position:absolute;left:7px;right:7px;display:flex;justify-content:space-between}
.row-main{top:236px}
.row-alt{top:640px}
.section-label{position:absolute;left:8px;top:606px;font:700 13px "Montserrat",sans-serif;color:var(--ink)}
.ad{width:384px;height:304px;background:var(--paper);position:relative;overflow:hidden;box-shadow:0 0 0 1px #e3e6e7}
.ad-visual{position:absolute;right:0;top:0;width:178px;height:272px}
.ad-visual .bg{position:absolute;inset:0}
.photo{position:absolute;right:8px;bottom:0;width:130px;height:200px;border-radius:65px 65px 0 0}
.photo.teal{background:linear-gradient(180deg,#c7a27c 0%,#8cb9c9 45%,#3f90b4 100%)}
.photo.lilac{background:linear-gradient(180deg,#d8c8b0 0%,#cdb3d8 45%,#9a86c8 100%)}
.photo.grey{background:linear-gradient(180deg,#e5e1dc 0%,#c9c2bb 50%,#9a8f86 100%)}
.balloons{position:absolute;left:-4px;top:24px;width:46px;height:64px;border-radius:23px;background:linear-gradient(160deg,#7cc14f,#38a9a9)}
.brand{position:absolute;left:46px;top:30px;display:flex;align-items:center;gap:5px;font:700 9px "Montserrat",sans-serif;color:var(--teal);background:rgba(255,255,255,.85);padding:3px 6px;border-radius:10px;white-space:nowrap}
.brand i{width:10px;height:10px;border-radius:50%;border:2px solid var(--teal);display:block}
.ad-text{position:absolute;left:16px;top:16px;width:196px}
.kicker{font:400 10.5px "Lora",serif;color:var(--muted);margin-bottom:3px}
.headline{font:700 17px/1.15 "Montserrat",sans-serif;color:var(--teal);white-space:nowrap}
.headline.green{color:var(--green)}
.lead{font-size:8.5px;line-height:1.4;margin:8px 0;color:var(--ink)}
.lead b{font-weight:700}
.sub{font:700 11px "Montserrat",sans-serif;color:var(--green);margin:6px 0 3px}
.list{list-style:none;font-size:8.5px;line-height:1.45}
.list li{position:relative;padding-left:10px}
.list li::before{content:"";position:absolute;left:0;top:4px;width:5px;height:5px;border-radius:50%;background:var(--green)}
.ad-footer{position:absolute;left:0;right:0;bottom:0;height:32px;background:var(--footer);display:flex;align-items:center;justify-content:space-between;gap:8px;padding:0 10px 0 16px}
.ad-footer .note{font:400 10px "Lora",serif;color:var(--teal);white-space:nowrap}
.ad-footer .url{background:var(--pill);color:var(--pill-text);font:600 8.5px "Montserrat",sans-serif;padding:4px 10px;border-radius:10px;white-space:nowrap}
</style>
</head>
<body>

<div class="row row-main">
  <article class="ad">
    <div class="ad-visual">
      <svg class="bg" viewBox="0 0 178 272"><path d="M60 0H178V272H0C40 200 20 80 60 0Z" fill="#eef1f2"/></svg>
      <div class="balloons" role="img" aria-label="Luftballons in Grün und Türkis"></div>
      <div class="brand"><i></i>Lindwerk Pflege</div>
      <div class="photo teal" role="img" aria-label="Pflegerin in türkisfarbener Kleidung zeigt Daumen hoch"></div>
    </div>
    <div class="ad-text">
      <p class="kicker">Feiern Sie mit uns!</p>
      <h2 class="headline">1-jähriges Jubiläum</h2>
      <h2 class="headline green">am 01.09.2024</h2>
      <p class="lead">Anlässlich unseres 1-jährigen Jubiläums möchten wir uns bei allen <b>Patienten, Angehörigen und Kooperationspartnern</b> für das Vertrauen bedanken.</p>
      <p class="sub">Besuchen Sie uns:</p>
      <ul class="list"><li>01. September 2024, 10:00 Uhr – 15:00</li><li>Ginsterweg 14, Dessau-Roßlau</li><li>Kostenlose Beratung vor Ort</li></ul>
    </div>
    <div class="ad-footer"><span class="note">Wir freuen uns auf dich!</span><span class="url">www.lindwerk-pflege.de</span></div>
  </article>

  <article class="ad">
    <div class="ad-visual">
      <svg class="bg" viewBox="0 0 178 272"><path d="M60 0H178V272H0C40 200 20 80 60 0Z" fill="#eef1f2"/></svg>
      <div class="brand" style="left:20px"><i></i>Lindwerk Pflege</div>
      <div class="photo grey" role="img" aria-label="Hauswirtschafterin mit Putzutensilien"></div>
    </div>
    <div class="ad-text">
      <p class="kicker">Kommt in unser Team!</p>
      <h2 class="headline green">Hauswirtschafter/in</h2>
      <p class="lead">Ziel ist uns die Pflege in der Umgebung Dessau-Roßlau qualitativ zu verbessern und kreativ mitzugestalten.</p>
      <p class="sub">Was bringst du mit:</p>
      <ul class="list"><li>Hilfsbereitschaft &amp; Engagement</li><li>Führerschein Klasse B</li><li>Gute Deutschkenntnisse in Wort und Schrift</li></ul>
      <p class="sub">Das bieten wir:</p>
      <ul class="list"><li>30 Tage Urlaub</li><li>Fort- &amp; Weiterbildungen, Sonderleistungen</li><li>Überdurchschnittliche Vergütung</li></ul>
    </div>
    <div class="ad-footer"><span class="note" style="font-size:9px">Wir freuen uns auf deine Bewerbung!</span><span class="url" style="font-size:7.5px;padding:4px 8px">www.lindwerk-pflege.de/karriere</span></div>
  </article>

  <article class="ad">
    <div class="ad-visual">
      <svg class="bg" viewBox="0 0 178 272"><path d="M60 0H178V272H0C40 200 20 80 60 0Z" fill="#eef1f2"/></svg>
      <div class="brand" style="left:30px"><i></i>Lindwerk Pflege</div>
      <div class="photo lilac" role="img" aria-label="Beraterin im Gespräch mit älterer Dame"></div>
    </div>
    <div class="ad-text">
      <p class="kicker">Lassen Sie sich beraten!</p>
      <h2 class="headline">Pflichtberatung</h2>
      <h2 class="headline green">bei Pflegegeldbezug</h2>
      <p class="lead">Gerne übernehmen wir für Sie den <b>Beratungseinsatz nach §37 Abs. 3 SGB XI</b>, wenn Sie dazu verpflichtet sind.</p>
      <ul class="list"><li>Verpflichtend für Pflegebedürftige, die <b>Pflegegeld</b> für die häusliche Pflege beziehen</li><li>Sofern Sie <b>keinerlei Hilfe</b> von einer professionellen Pflegekraft erhalten</li><li>Verpflichtend, in <b>regelmäßigen Abständen</b>, abhängig vom Pflegegrad</li></ul>
    </div>
    <div class="ad-footer"><span class="note">Nehmen Sie Kontakt mit uns auf!</span></div>
  </article>
</div>

<p class="section-label">Bildalternativen zu Anzeige 1</p>

<div class="row row-alt">
  <article class="ad">
    <div class="ad-visual">
      <svg class="bg" viewBox="0 0 178 272"><path d="M60 0H178V272H0C40 200 20 80 60 0Z" fill="#eef1f2"/></svg>
      <div class="balloons" role="img" aria-label="Luftballons in Grün und Türkis"></div>
      <div class="brand"><i></i>Lindwerk Pflege</div>
      <div class="photo teal" role="img" aria-label="Jubelnde Pflegerin in türkisfarbener Kleidung"></div>
    </div>
    <div class="ad-text">
      <p class="kicker">Feiern Sie mit uns!</p>
      <h2 class="headline">1-jähriges Jubiläum</h2>
      <h2 class="headline green">am 01.09.2024</h2>
      <p class="lead">Anlässlich unseres 1-jährigen Jubiläums möchten wir uns bei allen <b>Patienten, Angehörigen und Interessenten</b> für das Vertrauen bedanken.</p>
      <p class="sub">Besuchen Sie uns:</p>
      <ul class="list"><li>01. September 2024, 10:00 Uhr – 15:00</li><li>Ginsterweg 14, Dessau-Roßlau</li><li>Kostenlose Beratung vor Ort</li></ul>
    </div>
    <div class="ad-footer"><span class="note">Wir freuen uns auf dich!</span><span class="url">www.lindwerk-pflege.de</span></div>
  </article>

  <article class="ad">
    <div class="ad-visual">
      <svg class="bg" viewBox="0 0 178 272"><path d="M60 0H178V272H0C40 200 20 80 60 0Z" fill="#eef1f2"/></svg>
      <div class="balloons" role="img" aria-label="Luftballons in Grün und Türkis"></div>
      <div class="brand"><i></i>Lindwerk Pflege</div>
      <div class="photo teal" role="img" aria-label="Lachende Pflegerin in Nahaufnahme"></div>
    </div>
    <div class="ad-text">
      <p class="kicker">Feiern Sie mit uns!</p>
      <h2 class="headline">1-jähriges Jubiläum</h2>
      <h2 class="headline green">am 01.09.2024</h2>
      <p class="lead">Anlässlich unseres 1-jährigen Jubiläums möchten wir uns bei allen <b>Patienten, Angehörigen und Interessenten</b> für das Vertrauen bedanken.</p>
      <p class="sub">Besuchen Sie uns:</p>
      <ul class="list"><li>01. September 2024, 10:00 Uhr – 15:00</li><li>Ginsterweg 14, Dessau-Roßlau</li><li>Kostenlose Beratung vor Ort</li></ul>
    </div>
    <div class="ad-footer"><span class="note">Wir freuen uns auf dich!</span><span class="url">www.lindwerk-pflege.de</span></div>
  </article>

  <article class="ad">
    <div class="ad-visual">
      <svg class="bg" viewBox="0 0 178 272"><path d="M60 0H178V272H0C40 200 20 80 60 0Z" fill="#eef1f2"/></svg>
      <div class="balloons" role="img" aria-label="Luftballons in Grün und Türkis"></div>
      <div class="brand"><i></i>Lindwerk Pflege</div>
      <div class="photo teal" role="img" aria-label="Pflegerin mit langen Haaren ballt jubelnd die Faust"></div>
    </div>
    <div class="ad-text">
      <p class="kicker">Feiern Sie mit uns!</p>
      <h2 class="headline">1-jähriges Jubiläum</h2>
      <h2 class="headline green">am 01.09.2024</h2>
      <p class="lead">Anlässlich unseres 1-jährigen Jubiläums möchten wir uns bei allen <b>Patienten, Angehörigen und Interessenten</b> für das Vertrauen bedanken.</p>
      <p class="sub">Besuchen Sie uns:</p>
      <ul class="list"><li>01. September 2024, 10:00 Uhr – 15:00</li><li>Ginsterweg 14, Dessau-Roßlau</li><li>Kostenlose Beratung vor Ort</li></ul>
    </div>
    <div class="ad-footer"><span class="note">Wir freuen uns auf dich!</span><span class="url">www.lindwerk-pflege.de</span></div>
  </article>
</div>

</body>
</html>
```